Needing a business Card for new fire company.

Velm, sales fire equipment and parts. We also do tree clearing for the forest service. My logo will be attached to this. I am also looking for a design that when people see the card it stick with them and they will remember my sales team giving it to them.

```html
<!DOCTYPE html>
<html lang="en">
<head>
<meta charset="utf-8">
<title>Velm Business Card</title>
<link href="https://fonts.googleapis.com/css2?family=Arimo:wght@400;700&display=swap" rel="stylesheet">
<style>
  :root {
    --page: #1b1b1b;
    --card-dark: #222222;
    --card-white: #ffffff;
    --brand-red: #c4262c;
    --ink-dark: #1e1e1e;
    --text-light: #ffffff;
  }
  * { box-sizing: border-box; margin: 0; padding: 0; }
  html, body {
    width: 1200px; height: 988px; overflow: hidden;
    background: var(--page);
    font-family: "Arimo", Arial, sans-serif;
  }
  .card {
    position: absolute;
    left: 290px;
    width: 620px; height: 354px;
    border-radius: 4px;
    overflow: hidden;
    box-shadow: 0 10px 30px rgba(0,0,0,.5);
  }
  .card-front { top: 100px; background: var(--card-dark); display: flex; align-items: center; justify-content: center; }
  .card-back { top: 534px; background: var(--card-dark); }
  .wordmark {
    font-weight: 700;
    letter-spacing: 4px;
    text-transform: uppercase;
  }
  .card-front .wordmark { color: var(--text-light); font-size: 92px; }
  .back-shape { position: absolute; inset: 0; }
  .back-wordmark {
    position: absolute; left: 430px; top: 112px; width: 180px; text-align: center;
    color: var(--ink-dark); font-size: 50px;
  }
  .name-block { position: absolute; left: 32px; top: 88px; }
  .name-accent { position: absolute; left: 0; top: 8px; width: 14px; height: 40px; background: var(--brand-red); }
  .person-name { margin-left: 28px; color: var(--brand-red); font-weight: 700; font-size: 27px; letter-spacing: 1px; }
  .person-title { margin-left: 28px; color: var(--text-light); font-size: 15px; margin-top: 2px; }
  .address { position: absolute; left: 98px; top: 196px; color: var(--text-light); font-size: 13px; line-height: 17px; }
  .contacts { position: absolute; left: 76px; top: 236px; list-style: none; color: var(--text-light); font-size: 13px; }
  .contacts li { display: flex; align-items: center; gap: 8px; height: 18px; }
  .contacts svg { width: 12px; height: 12px; fill: var(--brand-red); flex: none; }
</style>
</head>
<body>
  <section class="card card-front">
    <span class="wordmark">Velm</span>
  </section>

  <section class="card card-back">
    <svg class="back-shape" viewBox="0 0 620 354" aria-hidden="true">
      <path d="M414 0 C 366 130, 430 286, 620 312 L620 0 Z" fill="#c4262c"/>
      <path d="M428 0 C 384 124, 446 270, 620 296 L620 0 Z" fill="#ffffff"/>
    </svg>
    <span class="wordmark back-wordmark">Velm</span>

    <div class="name-block">
      <span class="name-accent"></span>
      <p class="person-name">DALE HARROW</p>
      <p class="person-title">CEO/Founder</p>
    </div>

    <p class="address">P.O. Box 41 Marrel AB<br>Country Name 4820</p>

    <ul class="contacts">
      <li><svg viewBox="0 0 12 12"><path d="M2.5 1 L4.5 1 L5.3 3.5 L4 4.5 C4.6 6 6 7.4 7.5 8 L8.5 6.7 L11 7.5 L11 9.5 C11 10.3 10.3 11 9.5 11 C5 11 1 7 1 2.5 C1 1.7 1.7 1 2.5 1Z"/></svg>02 5550 0142</li>
      <li><svg viewBox="0 0 12 12"><path d="M3 0.5 H9 V11.5 H3 Z M4 1.5 V9.5 H8 V1.5 Z M5.5 10 H6.5 V11 H5.5 Z"/></svg>0400 555 217</li>
      <li><svg viewBox="0 0 12 12"><path d="M0.5 2.5 H11.5 V9.5 H0.5 Z M1.2 3 L6 6.6 L10.8 3 Z"/></svg>info@velmsupply.com</li>
      <li><svg viewBox="0 0 12 12"><circle cx="6" cy="6" r="5.5"/></svg>www.velmsupply.com</li>
    </ul>
  </section>
</body>
</html>
```